Business Cards for a law firm

Business cards for our law firm. Use our silhoette logo and OAK HARBOR - check our website (www.oakharbor-legal.com)

Contact Information for Business Card

our silhouette logo, OAK HARBOR, 800-555-0147, Dorian Kestrup, dorian@oakharbor-legal.com

Requirements
Must have
• our silhouette logo, OAK HARBOR, 800-555-0147, Dorian Kestrup, dorian@oakharbor-legal.com

```html
<!DOCTYPE html>
<html lang="en">
<head>
<meta charset="utf-8">
<title>Oak Harbor – Business Cards</title>
<link rel="stylesheet" href="https://fonts.googleapis.com/css2?family=Montserrat:wght@400;500;600;700&display=swap">
<style>
  :root {
    --backdrop: #3d4442;
    --paper: #ececec;
    --navy: #1e2b5c;
    --navy-light: #2c4a8f;
    --navy-mark: #24336b;
    --orange: #e39a1c;
    --white: #ffffff;
  }
  * { margin: 0; padding: 0; box-sizing: border-box; }
  html, body { width: 1200px; height: 1168px; overflow: hidden; }
  body {
    background: var(--backdrop);
    font-family: "Montserrat", sans-serif;
    position: relative;
  }
  .card {
    position: absolute;
    left: 246px;
    width: 701px;
    height: 400px;
    box-shadow: 4px 6px 10px rgba(0,0,0,0.35);
    overflow: hidden;
  }
  .card-front { top: 138px; background: var(--paper); }
  .card-back { top: 612px; background: var(--navy); }

  .brand {
    position: absolute;
    display: flex;
    align-items: center;
    white-space: nowrap;
  }
  .brand-mark { flex: none; }
  .brand-name { font-weight: 700; letter-spacing: 0.5px; }

  .card-front .brand { left: 111px; top: 58px; }
  .card-front .brand-mark {
    width: 42px; height: 42px;
    background: var(--navy);
    margin-right: 12px;
  }
  .card-front .brand-name { font-size: 28px; color: var(--navy); }

  .card-back .brand { left: 0; right: 0; top: 158px; justify-content: center; }
  .card-back .brand-mark {
    width: 58px; height: 58px;
    background: var(--navy-mark);
    margin-right: 18px;
  }
  .card-back .brand-name { font-size: 44px; color: var(--navy-light); }

  .person {
    position: absolute;
    right: 372px; top: 215px;
    text-align: right;
  }
  .person-name {
    font-size: 19.5px;
    font-weight: 700;
    letter-spacing: 1.2px;
    color: var(--navy);
    text-transform: uppercase;
    white-space: nowrap;
  }
  .person-name .surname { color: var(--orange); }
  .person-role {
    font-size: 16.5px;
    font-weight: 500;
    color: var(--navy);
    letter-spacing: 0.5px;
    margin-top: 1px;
  }
  .divider {
    position: absolute;
    left: 351px; top: 208px;
    width: 2px; height: 80px;
    background: var(--orange);
  }
  .contact {
    position: absolute;
    left: 376px; top: 215px;
    list-style: none;
  }
  .contact li {
    display: flex; align-items: center;
    height: 23px;
    font-size: 17px;
    font-weight: 500;
    color: var(--navy);
    letter-spacing: 0.3px;
    white-space: nowrap;
  }
  .contact svg { width: 14px; height: 14px; margin-right: 10px; flex: none; }

  .band-accent {
    position: absolute;
    left: 0; bottom: 0;
    width: 100%; height: 29px;
  }
  .tagline {
    position: absolute;
    right: 84px; bottom: 6px;
    font-size: 13px;
    font-weight: 500;
    letter-spacing: 2.6px;
    color: var(--white);
  }
</style>
</head>
<body>
  <section class="card card-front">
    <div class="brand">
      <span class="brand-mark" role="img" aria-label="Firm logo mark"></span>
      <span class="brand-name">OAK HARBOR</span>
    </div>

    <div class="person">
      <div class="person-name">Dorian <span class="surname">Kestrup</span></div>
      <div class="person-role">Attorney</div>
    </div>
    <div class="divider"></div>
    <ul class="contact">
      <li>
        <svg viewBox="0 0 24 24" aria-hidden="true"><path fill="#e39a1c" d="M6.6 10.8a15.1 15.1 0 0 0 6.6 6.6l2.2-2.2c.3-.3.7-.4 1-.2 1.1.4 2.3.6 3.6.6.6 0 1 .4 1 1V20c0 .6-.4 1-1 1A17 17 0 0 1 3 4c0-.6.4-1 1-1h3.5c.6 0 1 .4 1 1 0 1.3.2 2.5.6 3.6.1.3 0 .7-.2 1z"/></svg>
        800-555-0147
      </li>
      <li>
        <svg viewBox="0 0 24 24" aria-hidden="true" fill="none" stroke="#e39a1c" stroke-width="1.8"><rect x="2.5" y="5" width="19" height="14" rx="1.5"/><path d="M3 6l9 7 9-7"/></svg>
        dorian@oakharbor-legal.com
      </li>
      <li>
        <svg viewBox="0 0 24 24" aria-hidden="true" fill="none" stroke="#e39a1c" stroke-width="1.8"><circle cx="12" cy="12" r="9.5"/><ellipse cx="12" cy="12" rx="4" ry="9.5"/><path d="M2.5 12h19M4 7h16M4 17h16"/></svg>
        www.oakharbor-legal.com
      </li>
    </ul>

    <svg class="band-accent" viewBox="0 0 701 29" preserveAspectRatio="none" aria-hidden="true">
      <polygon points="0,17 311,17 304,29 0,29" fill="#e39a1c"/>
      <polygon points="322,0 701,0 701,29 307,29" fill="#1e2b5c"/>
    </svg>
    <div class="tagline">INJURY ATTORNEYS</div>
  </section>

  <section class="card card-back">
    <div class="brand">
      <span class="brand-mark" role="img" aria-label="Firm logo mark"></span>
      <span class="brand-name">OAK HARBOR</span>
    </div>
  </section>
</body>
</html>
```